Need Help having my business card stand out

I am the owner of Pine Ridge Canine Coaching and would like for my business cards to stand out. I have been trying to keep designing them myself but I can't get what I have in my head on the card. I will try my best to post templates that I like for inspirations. I want something unique but elegant. I don't want in to look cartoony or cheesy. It needs to pop in a pet shop but also in a coffee shop or gym.

Target Market(s)

Dog owners, Married ,No young kids Jr High school kids and up (maybe kids on the way) Executives, Stay at home moms/wives, Small business owners

Industry/Entity Type

Dog Training

Contact Information for Business Card

Trevor Holloway, 555-304-7162, info@pineridgecanine.example, www.pineridgecanine.example

Colors

Designer to choose colors to be used in the design.

Requirements
Must have
• my logo
Should not have
• Cursive lettering

```html
<!DOCTYPE html>
<html lang="en">
<head>
<meta charset="utf-8">
<title>Pine Ridge Canine Coaching – Business Card</title>
<link href="https://fonts.googleapis.com/css2?family=Saira+Condensed:wght@400;600&display=swap" rel="stylesheet">
<style>
  :root {
    --backdrop: #e9e9e7;
    --card-white: #ffffff;
    --ink: #111111;
    --photo-light: #e6e4b4;
    --photo-mid: #7f955a;
    --photo-dark: #2e3b22;
  }
  * { box-sizing: border-box; margin: 0; padding: 0; }
  html, body { width: 1200px; height: 863px; overflow: hidden; }
  body {
    background: var(--backdrop);
    font-family: "Saira Condensed", "Arial Narrow", sans-serif;
    color: var(--ink);
    position: relative;
  }
  .card {
    position: absolute;
    top: 169px;
    width: 300px;
    height: 525px;
    overflow: hidden;
    box-shadow: 0 8px 24px rgba(0,0,0,0.18);
  }
  .card--front { left: 270px; }
  .card--back { left: 630px; background: var(--card-white); }

  .front-photo {
    position: absolute; inset: 0;
    background:
      radial-gradient(ellipse at 50% 15%, var(--photo-light) 0%, transparent 55%),
      linear-gradient(180deg, var(--photo-light) 0%, var(--photo-mid) 45%, var(--photo-dark) 100%);
  }
  .front-brand {
    position: absolute; top: 40px; right: 22px;
    width: 110px; text-align: right;
    font-weight: 600; font-size: 15px; line-height: 1.05;
    text-transform: uppercase; color: var(--ink);
  }

  .back-tagline {
    position: absolute; top: 62px; left: 0; right: 0;
    text-align: center; font-size: 12px; letter-spacing: 2px;
    text-transform: uppercase;
  }
  .back-brand {
    position: absolute; top: 95px; left: 30px; right: 30px;
    text-align: center; font-weight: 600; font-size: 40px;
    line-height: 0.95; text-transform: uppercase;
  }
  .back-brand-mark {
    display: block; width: 14px; height: 14px; border-radius: 50%;
    background: var(--ink); margin: 0 auto 10px;
  }
  .name-rule { position: absolute; left: 22px; width: 256px; height: 2px; }
  .name-rule--top { top: 272px; }
  .name-rule--bottom { top: 320px; }
  .back-name {
    position: absolute; top: 280px; left: 0; right: 0;
    text-align: center; font-size: 24px; letter-spacing: 0.5px;
    text-transform: uppercase;
  }
  .back-contact {
    position: absolute; top: 380px; left: 0; right: 0;
    text-align: center; font-size: 15px; line-height: 1.35;
  }
  .back-band {
    position: absolute; left: 0; right: 0; bottom: 0; height: 14px;
    background: var(--ink);
  }
</style>
</head>
<body>
  <section class="card card--front">
    <div class="front-photo" role="img" aria-label="Posterized photo of a dog trainer standing on grass with a seated dog in a sunny park"></div>
    <div class="front-brand">Pine Ridge Canine Coaching</div>
  </section>

  <section class="card card--back">
    <p class="back-tagline">Your dog trainer for life</p>
    <div class="back-brand">
      <span class="back-brand-mark"></span>
      Pine Ridge Canine Coaching
    </div>

    <svg class="name-rule name-rule--top" viewBox="0 0 256 2" aria-hidden="true">
      <line x1="0" y1="1" x2="10" y2="1" stroke="#111" stroke-width="2"/>
      <line x1="18" y1="1" x2="238" y2="1" stroke="#111" stroke-width="2"/>
      <line x1="246" y1="1" x2="256" y2="1" stroke="#111" stroke-width="2"/>
    </svg>
    <h1 class="back-name" style="font-weight:400">Trevor Holloway</h1>
    <svg class="name-rule name-rule--bottom" viewBox="0 0 256 2" aria-hidden="true">
      <line x1="0" y1="1" x2="10" y2="1" stroke="#111" stroke-width="2"/>
      <line x1="18" y1="1" x2="238" y2="1" stroke="#111" stroke-width="2"/>
      <line x1="246" y1="1" x2="256" y2="1" stroke="#111" stroke-width="2"/>
    </svg>

    <address class="back-contact" style="font-style:normal">
      555-304-7162<br>
      info@pineridgecanine.example<br>
      www.pineridgecanine.example
    </address>
    <div class="back-band"></div>
  </section>
</body>
</html>
```